Business card design for upmarket Home Technology design and Installation company

Hello designers, we need a great business card designed.
We need it to convey high tech, and also sophistication .
We work with some of the most affluent people in the world building them home technology systems, and A/V entertainment systems.

Services offered include the following:
Design, sales, installation, and maintenance of

*Home Automation systems
*Distributed / Multi-Room Audio and Video
*High Performance Networks & WiFi
* Lighting and Shade Control
*Home cinema
*Security and CCTV Systems

I have included a copy of our logo to use for your design efforts.

Target Market(s)

Upmarket clients with multi million euro villas.

Industry/Entity Type

Home technology

Contact Information for Business Card

NAME: Derek Halvin ADDRESS: Carrer Bellamar Local 42, Cala Torrent, 07293 PHONE: +34-652-918-204 EMAIL: DHalvin@VORTELhomesystems.example WEB: www.vortelhomesystems.example

Requirements
Must have
• Our Logo, and our tagline

```html
<!DOCTYPE html>
<html lang="en">
<head>
<meta charset="utf-8">
<title>VORTEL Business Card</title>
<link href="https://fonts.googleapis.com/css2?family=Outfit:wght@300;400;700&display=swap" rel="stylesheet">
<style>
  :root {
    --backdrop: #d0d0d0;
    --card: #ffffff;
    --ink: #1d1d1f;
    --faint: #e8e8e8;
    --shadow: rgba(0,0,0,0.12);
  }
  html, body {
    margin: 0;
    padding: 0;
    width: 1200px;
    height: 1000px;
    overflow: hidden;
    background: var(--backdrop);
    font-family: 'Outfit', sans-serif;
    color: var(--ink);
  }
  .canvas { position: relative; width: 1200px; height: 1000px; }
  .card {
    position: absolute;
    left: 262px;
    width: 678px;
    height: 387px;
    background: var(--card);
    border-radius: 28px;
    overflow: hidden;
    box-shadow: 4px 6px 10px var(--shadow);
  }
  .card-front { top: 72px; }
  .card-back { top: 500px; }

  .brand {
    display: flex;
    flex-direction: column;
    align-items: center;
  }
  .brand-mark { border-radius: 50%; background: var(--ink); }
  .brand-name {
    font-weight: 400;
    letter-spacing: 0.22em;
    color: var(--ink);
    line-height: 1;
  }
  .card-front .brand {
    position: absolute;
    left: 0; right: 0; top: 62px;
  }
  .card-front .brand-mark { width: 64px; height: 64px; margin-bottom: 34px; }
  .card-front .brand-name { font-size: 34px; padding-left: 0.22em; }
  .front-web {
    position: absolute;
    left: 0; right: 0; top: 338px;
    text-align: center;
    font-size: 15px;
    font-weight: 400;
  }

  .back-decor {
    position: absolute;
    left: 318px; top: 40px;
    width: 380px; height: 380px;
    border-radius: 50%;
    background: var(--faint);
  }
  .card-back .brand {
    position: absolute;
    left: 24px; top: 30px;
    width: 84px;
  }
  .card-back .brand-mark { width: 30px; height: 30px; margin-bottom: 24px; }
  .card-back .brand-name { font-size: 17px; padding-left: 0.22em; }
  .holder-name {
    position: absolute;
    right: 24px; top: 38px;
    margin: 0;
    font-size: 46px;
    font-weight: 700;
    letter-spacing: 0.01em;
    line-height: 1;
  }
  .name-rule {
    position: absolute;
    right: 24px; top: 94px;
    width: 56px; height: 2px;
    background: var(--ink);
  }
  .contact-rule {
    position: absolute;
    left: 24px; right: 24px; top: 290px;
    height: 5px;
    background: var(--ink);
  }
  .contact {
    position: absolute;
    top: 303px;
    font-size: 15px;
    font-weight: 300;
    line-height: 19px;
  }
  .contact-left { left: 26px; }
  .contact-right { right: 32px; text-align: right; }
  .contact-row { display: flex; }
  .contact-label { width: 68px; }
</style>
</head>
<body>
<div class="canvas">
  <section class="card card-front">
    <div class="brand">
      <div class="brand-mark"></div>
      <div class="brand-name">VORTEL</div>
    </div>
    <div class="front-web">www.vortelhomesystems.example</div>
  </section>

  <section class="card card-back">
    <div class="back-decor"></div>
    <div class="brand">
      <div class="brand-mark"></div>
      <div class="brand-name">VORTEL</div>
    </div>
    <h1 class="holder-name">DEREK HALVIN</h1>
    <div class="name-rule"></div>
    <div class="contact-rule"></div>
    <div class="contact contact-left">
      <div class="contact-row"><span>Phone:&nbsp;+34-652-918-204</span></div>
      <div class="contact-row"><span class="contact-label">Address:</span><span>Carrer Bellamar, Local 42,<br>07293 Cala Torrent,</span></div>
    </div>
    <div class="contact contact-right">
      <div>Email: dhalvin@vortelhomesystems.example</div>
      <div>Website: www.vortelhomesystems.example</div>
    </div>
  </section>
</div>
</body>
</html>
```